Fact/Marketing Sheet(s) for Health & Wellness Plan

We are wanting to market a new program that we have for Health & Wellness Benefits for our customer Kestrel Federation of Township Guilds (KFTG). We would like to present this information in a professional format that compels the recipient/reader to act on this.
I like the format of the TofB document (see attahed)- however would adjust the photo to be something Agricultural related.
I am very interested to see other ideas that may be proposed.
In addition to the content that we are wanting to communicate at this time (see attached (KFTG Project ) I have also included our Style Guide , logos, and pattern if needed.
Members of the Kestrel Federation of Township Guilds - typically business leaders and volunteers in communities across Alberta.
- In Brand Document

```html
<!DOCTYPE html>
<html lang="en">
<head>
<meta charset="utf-8">
<title>Health &amp; Wellness Benefit Program – Fact Sheets</title>
<link rel="stylesheet" href="https://fonts.googleapis.com/css2?family=Archivo:wght@700;800&family=Oswald:wght@700&family=Zilla+Slab:wght@700&family=Open+Sans:wght@400;600&family=Arimo:wght@400;700&family=Tinos&display=swap">
<style>
:root{
  --teal-dark:#0f5a5c;
  --green:#1f9a55;
  --navy:#1c3f94;
  --bar-blue:#1d47a4;
  --slate:#83a096;
  --ink:#1a1a1a;
  --muted:#4a4a4a;
  --gold:#e9d48a;
  --tile:#e7d58c;
  --page-border:#9a9a9a;
}
*{margin:0;padding:0;box-sizing:border-box}
html,body{width:848px;height:1200px;overflow:hidden;background:#fff}
body{position:relative;font-family:"Open Sans",sans-serif;color:var(--ink)}
.sheet{position:absolute;width:396px;height:581px;border:1px solid var(--page-border);overflow:hidden;background:#fff}
.sheet--tl{left:25px;top:20px}
.sheet--tr{left:429px;top:20px}
.sheet--bl{left:25px;top:600px}
.sheet--br{left:429px;top:600px}
.abs{position:absolute}

/* header */
.club-mark{position:absolute;top:19px;left:0;width:100%;display:flex;justify-content:center;align-items:center;gap:6px}
.club-mark__dot{width:16px;height:16px;border-radius:50%;background:var(--green)}
.club-mark__name{font-family:"Arimo",sans-serif;font-weight:700;font-size:9.5px;line-height:11px;color:var(--teal-dark);text-transform:uppercase}
.banner{position:absolute;left:0;top:78px;width:100%;height:110px;
  background:linear-gradient(180deg,#eef3e4 0%,#dfe9cf 35%,#c9dca8 60%,#b8d08f 80%,#d7d9a3 100%)}
.banner-title{position:absolute;left:0;width:100%;text-align:center;line-height:1}
.banner-title--sans{font-family:"Archivo",sans-serif;font-weight:800;color:var(--teal-dark)}
.banner-title--serif{font-family:"Zilla Slab",serif;font-weight:700;color:var(--teal-dark)}

/* broker sign-off */
.broker{position:absolute;left:253px;top:537px;display:flex;align-items:center;gap:6px}
.broker__dot{width:20px;height:20px;border-radius:50%;background:var(--navy)}
.broker__name{font-family:"Zilla Slab",serif;font-weight:700;font-size:12px;color:var(--navy);letter-spacing:.3px}

/* contact block */
.contact{position:absolute;font-family:"Tinos",serif;color:var(--teal-dark)}
.contact p{font-size:10.5px;line-height:16.5px}
.contact .contact__mail{font-size:8.5px;line-height:16px}

/* side rule */
.side-rule{position:absolute;left:22px;top:210px;width:14px;height:117px;background:var(--slate)}

/* page 1 */
.field-bg{position:absolute;left:0;top:188px;width:100%;height:393px;
  background:linear-gradient(180deg,#cfe6f4 0%,#e4f0ef 30%,#f2eec8 55%,#f4e6a6 80%,#f0d98a 100%)}
.highlights-title{position:absolute;top:205px;width:100%;text-align:center;font-family:"Oswald",sans-serif;font-weight:700;font-size:24px;color:var(--green)}
.highlights-sub{position:absolute;top:237px;left:30px;width:336px;text-align:center;font-family:"Tinos",serif;font-size:10.5px;line-height:14px;color:#555}
.tile{position:absolute;top:279px;width:69px;height:82px;background:var(--tile);display:flex;align-items:center;justify-content:center}
.tile svg{width:48px;height:48px}
.tile-caption{position:absolute;top:367px;width:100px;text-align:center;font-family:"Arimo",sans-serif;font-size:7px;line-height:9px;color:#333}
.coverage-title{position:absolute;left:33px;top:407px;font-family:"Arimo",sans-serif;font-weight:700;font-size:10.5px}
.coverage-list{position:absolute;left:33px;top:421px;list-style:none;font-size:9px;line-height:12.5px}
.coverage-list li span{display:inline-block;width:19px}
.apply-box{position:absolute;left:279px;top:463px;width:104px;height:70px;background:rgba(214,222,140,.55);
  font-family:"Tinos",serif;font-size:7.3px;line-height:10.4px;color:#555;text-align:center;padding-top:7px}
.blue-bar{position:absolute;left:0;top:542px;width:250px;height:13px;background:var(--bar-blue)}

/* page 2 */
.fact-list{position:absolute;left:42px;font-family:"Arimo",sans-serif;font-size:7.6px;line-height:10.3px;color:var(--ink)}
.fact-list h3{font-size:8.5px;font-weight:700;line-height:11px}
.fact-list ol{list-style:none}
.fact-list li{display:flex}
.fact-list li span{width:16px;flex:none}
.badge{position:absolute;top:346px;width:52px;height:52px;border-radius:50%;
  background:radial-gradient(circle at 40% 35%,#fbf0bf 0%,#ecd98e 60%,#dcc373 100%);
  box-shadow:0 1px 3px rgba(0,0,0,.25);
  display:flex;align-items:center;justify-content:center;font-family:"Zilla Slab",serif;font-weight:700;font-size:23px;color:var(--teal-dark)}
.badge-label{position:absolute;top:405px;width:80px;text-align:center;font-family:"Arimo",sans-serif;font-size:7.2px;line-height:9.4px;color:#333}
.badge-label b{display:block;font-size:8.5px;color:#2c5a8a;font-weight:700}
.badge-label strong{display:block;color:#000}
.family-photo{position:absolute;left:0;top:464px;width:232px;height:98px;background:linear-gradient(120deg,#b98d6c 0%,#d8b596 50%,#e9d6c2 100%)}

/* page 3 */
.care-bg{position:absolute;left:0;top:188px;width:100%;height:393px;background:linear-gradient(180deg,#ffffff 0%,#f5f9fb 40%,#d8edf2 70%,#c9e5ee 100%)}
.shield-art{position:absolute;left:60px;top:375px;width:125px;height:160px;border-radius:10px 10px 62px 62px;background:linear-gradient(180deg,rgba(255,255,255,.7),rgba(178,218,228,.7))}
.fees-title{position:absolute;left:46px;top:206px;font-family:"Zilla Slab",serif;font-weight:700;font-size:17px;color:#4a5a5a}
.fees-list{position:absolute;left:65px;top:232px;width:275px;list-style:none;font-size:7.6px;line-height:10.7px}
.fees-list li{display:flex}
.fees-list li span{width:16px;flex:none}
.fees-list li.fade{color:#5f6a73}
.t4-note{position:absolute;left:80px;top:411px;font-family:"Tinos",serif;font-size:8.3px;color:#5a6870}

/* page 4 */
.doctor-bg{position:absolute;left:0;top:188px;width:100%;height:393px;background:linear-gradient(100deg,#e6eef2 0%,#f2f5f6 35%,#fafafa 60%,#f2f3f3 100%)}
.efap{position:absolute;left:51px;top:207px;font-family:"Arimo",sans-serif;color:var(--ink)}
.efap h3{font-size:9.4px;font-weight:700;line-height:12px}
.efap ol{list-style:none;font-size:8.8px;line-height:12px}
.efap li span{display:inline-block;width:15px}
.plain{position:absolute;left:50px;font-family:"Arimo",sans-serif;font-size:8.8px;line-height:12.5px;color:#222;width:330px}
.plain--tight{line-height:11.5px}
</style>
</head>
<body>

<!-- Sheet 1: Program overview -->
<section class="sheet sheet--tl">
  <div class="club-mark"><span class="club-mark__dot"></span><span class="club-mark__name">Kestrel Federation of<br>Township Guilds</span></div>
  <div class="banner" role="img" aria-label="Illustrated rolling farmland with fields, trees and barns"></div>
  <h1 class="banner-title banner-title--sans" style="top:126px;font-size:27px">HEALTH &amp; WELLNESS</h1>
  <h2 class="banner-title banner-title--sans" style="top:157px;font-size:19px;color:var(--green)">Benefit Program</h2>

  <div class="field-bg" role="img" aria-label="Soft sky fading into a golden wheat field"></div>
  <h2 class="highlights-title">Program Highlights</h2>
  <p class="highlights-sub">Flexible coverage options with the ability to build your own plan that is best for your employees and board members</p>

  <div class="tile" style="left:32px"><svg viewBox="0 0 48 48"><path d="M24 4 L42 10 V24 C42 35 34 42 24 46 C14 42 6 35 6 24 V10 Z" fill="#2aa36a"/><path d="M24 9 V24 H10 V12 Z M24 24 H38 C38 33 31 39 24 42 Z" fill="#e7d58c"/></svg></div>
  <div class="tile" style="left:118px"><svg viewBox="0 0 48 48"><circle cx="24" cy="19" r="14" fill="#2aa36a"/><circle cx="24" cy="19" r="9" fill="#e7d58c"/><path d="M24 13 l2 4 4 .5-3 3 .8 4-3.8-2-3.8 2 .8-4-3-3 4-.5z" fill="#2aa36a"/><path d="M14 29 L8 42 L14 40 L17 45 L22 32 Z M34 29 L40 42 L34 40 L31 45 L26 32 Z" fill="#2aa36a"/></svg></div>
  <div class="tile" style="left:205px"><svg viewBox="0 0 48 48"><circle cx="24" cy="24" r="19" fill="none" stroke="#2aa36a" stroke-width="4"/><path d="M24 11 l4 8 9 1-6.5 6 1.7 9-8.2-4.5-8.2 4.5 1.7-9-6.5-6 9-1z" fill="#2aa36a"/></svg></div>
  <div class="tile" style="left:293px"><svg viewBox="0 0 48 48"><rect x="3" y="9" width="38" height="27" rx="3" fill="#2aa36a"/><rect x="3" y="15" width="38" height="4" fill="#e7d58c"/><rect x="8" y="26" width="5" height="3" fill="#e7d58c"/><rect x="15" y="26" width="5" height="3" fill="#e7d58c"/><circle cx="37" cy="34" r="9" fill="#2aa36a" stroke="#e7d58c" stroke-width="2"/><path d="M33 34 l3 3 5-6" stroke="#fff" stroke-width="2.5" fill="none"/></svg></div>

  <p class="tile-caption" style="left:17px;width:100px;top:371px">Added protection for your employees/board members and their families</p>
  <p class="tile-caption" style="left:104px">Guaranteed issue with no medical underwriting</p>
  <p class="tile-caption" style="left:190px;width:100px;top:364px">Exclusive to existing members of the Kestrel Federation Of Township Guilds</p>
  <p class="tile-caption" style="left:278px">Simple and easy enrollment with convenient payment options</p>

  <h3 class="coverage-title">Coverages Available</h3>
  <ol class="coverage-list">
    <li><span>1.</span>Health Spending Accounts / Taxable Wellness Accounts</li>
    <li><span>2.</span>Life &amp; Disability Insurance</li>
    <li><span>3.</span>Critical Illness</li>
    <li><span>4.</span>Employee &amp; Family Assistance Program</li>
    <li><span>5.</span>Medical Second Opinion</li>
    <li><span>6.</span>Accidental Death and Dismemberment</li>
    <li><span>7.</span>Hospital Cash</li>
    <li><span>8.</span>Final Expenses</li>
  </ol>

  <div class="apply-box">To apply, please contact<br>our broker partner,<br>Harrow Lane Brokers<br>at (555) 014-2287<br>benefit@harrowlane.example</div>
  <div class="blue-bar"></div>
  <div class="broker"><span class="broker__dot"></span><span class="broker__name">HARROW LANE BROKERS</span></div>
</section>

<!-- Sheet 2: Insurance coverages -->
<section class="sheet sheet--tr">
  <div class="club-mark"><span class="club-mark__dot"></span><span class="club-mark__name">Kestrel Federation of<br>Township Guilds</span></div>
  <div class="banner" role="img" aria-label="Illustrated rolling farmland with fields, trees and barns"></div>
  <h1 class="banner-title banner-title--serif" style="top:89px;font-size:19px">Critical Illness</h1>
  <h1 class="banner-title banner-title--serif" style="top:112px;font-size:19px">Final Expense</h1>
  <h1 class="banner-title banner-title--serif" style="top:135px;font-size:19px">AD&amp;D</h1>
  <h1 class="banner-title banner-title--serif" style="top:155px;font-size:19px">Hospital Cash</h1>

  <div class="side-rule"></div>
  <div class="fact-list" style="top:208px">
    <h3>Coverage Available Up to Age 70 for:</h3>
    <ol>
      <li><span>1.</span>Employees</li>
      <li><span>2.</span>Board Members</li>
      <li><span>3.</span>Spouses and dependent children of employees or board members</li>
    </ol>
  </div>
  <div class="fact-list" style="top:259px;width:285px">
    <h3>Coverage Highlights:</h3>
    <ol>
      <li><span>1.</span>Simple and quick application process</li>
      <li><span>2.</span>Portable coverage that the employee/board member can take with them if they leave their employer</li>
      <li><span>3.</span>24/7 protection whether you are working, at home, or travelling</li>
      <li><span>4.</span>23 covered critical illness conditions including heart attack, stroke and cancer</li>
    </ol>
  </div>

  <div class="badge" style="left:43px">01</div>
  <div class="badge" style="left:128px">02</div>
  <div class="badge" style="left:213px">03</div>
  <div class="badge" style="left:298px">04</div>
  <p class="badge-label" style="left:29px"><b>Critical Illness</b>(Up to $150,000)<strong>$25,000 Guaranteed</strong></p>
  <p class="badge-label" style="left:114px"><b>Final Expense</b>(Up to $25,000)</p>
  <p class="badge-label" style="left:199px"><b>Accidental Death &amp; Dismemberment</b>(Up to $500,000)</p>
  <p class="badge-label" style="left:284px"><b>Hospital Cash</b>(Up to $250/day)</p>

  <div class="family-photo" role="img" aria-label="Photo of cupped hands holding a paper cut-out family"></div>
  <div class="contact" style="left:243px;top:460px">
    <p>For a quote,</p><p>please contact us</p><p>at (555) 014-2287</p><p class="contact__mail">benefit@harrowlane.example</p>
  </div>
  <div class="broker"><span class="broker__dot"></span><span class="broker__name">HARROW LANE BROKERS</span></div>
</section>

<!-- Sheet 3: Spending accounts -->
<section class="sheet sheet--bl">
  <div class="club-mark"><span class="club-mark__dot"></span><span class="club-mark__name">Kestrel Federation of<br>Township Guilds</span></div>
  <div class="banner" role="img" aria-label="Illustrated rolling farmland with fields, trees and barns"></div>
  <h1 class="banner-title banner-title--serif" style="top:99px;font-size:24px">Healthcare &amp; Wellness</h1>
  <h1 class="banner-title banner-title--serif" style="top:129px;font-size:28px">Spending Accounts</h1>

  <div class="care-bg" role="img" aria-label="Pale blue medical background with faint hexagon pattern"></div>
  <div class="shield-art" role="img" aria-label="Translucent shield with a medical cross"></div>
  <div class="side-rule"></div>
  <h2 class="fees-title">No Start up Fees</h2>
  <ol class="fees-list">
    <li><span>1.</span>A health care spending account offers comprehensive health &amp; dental benefits while giving your employees the flexibility to choose how they spend their health care dollars.</li>
    <li><span>2.</span>Taxable wellness accounts provide employees with the means to proactively manage their physical, mental and financial well-being. Gym memberships, vitamins and supplements, and many other wellness expenses are available under this benefit.</li>
    <li><span>3.</span>Travel insurance can be provided for your employees in addition to your health spending account.</li>
    <li class="fade"><span>4.</span>Virtual health care can be added by the employee to their plan for them and their family.</li>
    <li class="fade"><span>5.</span>Traditional group benefit plans are available which include life and disability insurance. Available to employers with 3 or more employees.</li>
  </ol>
  <p class="t4-note">Coverage is available to T4’d employees only and their families</p>

  <div class="contact" style="left:253px;top:464px">
    <p>For a quote,</p><p>please contact us</p><p>at (555) 014-2287</p><p class="contact__mail">benefit@harrowlane.example</p>
  </div>
  <div class="broker"><span class="broker__dot"></span><span class="broker__name">HARROW LANE BROKERS</span></div>
</section>

<!-- Sheet 4: EFAP and second opinion -->
<section class="sheet sheet--br">
  <div class="club-mark"><span class="club-mark__dot"></span><span class="club-mark__name">Kestrel Federation of<br>Township Guilds</span></div>
  <div class="banner" role="img" aria-label="Illustrated rolling farmland with fields, trees and barns"></div>
  <h1 class="banner-title banner-title--serif" style="top:102px;font-size:19px">Employee Family Assistance Program</h1>
  <h1 class="banner-title banner-title--serif" style="top:128px;font-size:19px">And Medical&nbsp; Second Opinion</h1>

  <div class="doctor-bg" role="img" aria-label="Soft photo of a medical professional holding a stethoscope"></div>
  <div class="side-rule"></div>
  <div class="efap">
    <h3>Coverage Available for:</h3>
    <ol>
      <li><span>1.</span>Employees</li>
      <li><span>2.</span>Board Members</li>
      <li><span>3.</span>Spouses and dependent children of employees or board<br><span></span>members</li>
    </ol>
  </div>
  <p class="plain" style="top:284px">Immediate&nbsp; and confidential access to variety of programs and services to help with work and life issues before they become more serious</p>
  <p class="plain plain--tight" style="top:315px">Service include, but are not limited to :<br>1. Short term counselling<br>2. Legal advice<br>3. Financial Planning<br>4. Nutritional Counselling<br>5. And much more</p>
  <p class="plain plain--tight" style="top:405px">Medical Second Opinion provides an independent review of diagnoses and treatment recomendations. These reviews are completed by medical professionals trained at some of the top medical institution in the world</p>

  <div class="contact" style="left:253px;top:463px">
    <p>To apply</p><p>please contact us</p><p>at (555) 014-2287</p><p class="contact__mail">benefit@harrowlane.example</p>
  </div>
  <div class="broker" style="top:534px"><span class="broker__dot"></span><span class="broker__name">HARROW LANE BROKERS</span></div>
</section>

</body>
</html>
```